Creative Brief
Marketing Collateral for Real Estate Business
Create matching postcards and Business Card.
MARKETING COLLATERAL FOR REAL ESTATE COMPANY
Create matching postcards, HTML email template and Business Card.
Postcard (5.5” x 8.5”) template
Email HTML template
Business Card
DESCRIPTION
Our office needs 2-3 “Just Listed” postcard templates for REAL ESTATE FORECLOSURE LISITNGS. The templates must display two logos which are provided (FindMarlowHomesteads.example to be large in size). We need the ability to insert pictures of each new listing inside within the template. The design must be colorful (earth tone colors), professional, simple and eye catching. Postcard: We also want 1-2 generic postcard templates where a standard/general real estate picture is already inserted which can be used for multiple/different properties.
Postcard templates must meet the printing specifications for PressNook.example. The templates must be provided in digital formats that are editable by the project holder. They must also be provided in print ready formats. Our company is based in Charleston, SC, USA. Please view images of Charleston, SC, USA via google if necessary for the postcard template.
The HTML Email Template(s) will be used to mass email our database with new listings.
Real Estate
Buyers of Real Estate Foreclosed Properties; Real Estate Investors.
DESIGN
POSTCARD COMMENTS / STATEMENTS TO BE INCLUDED WITHIN THE POSTCARD / EMAIL HTML
-PRE-LISTING(1-2 Templates)
-JUST LISTED (1-2 Templates)
-SEARCH HUNDREDS OF BANK OWNED FORECLOSURES – SIGN UP FREE! FINDMARLOWHOMESTEADS.EXAMPLE
-Join FindMarlowHomesteads.example and be the first to know about newly listed Charleston Foreclosures.
-Don’t miss this opportunity to buy a bank owned foreclosure.
-We are your Charleston Foreclosure Specialist!
-NEW LISTING ALERT – Sign up and receive listings meeting your criteria today! (in a highlighted icon or box or similar)
-This property is NOT listed in MLS yet. Please contact me if you are interested in purchasing this property. (disclaimer/small font))
POSTCARD SIZE
Postcard 5.5” x 8.5”
COLORS
Blue / Green / Tan (Earth tone colors) / To match FindMarlowHomesteads.example logo
Color (front and back)
Images and Date to be used

```html
<!DOCTYPE html>
<html lang="en">
<head>
<meta charset="utf-8">
<title>Post Card – Marketing Collateral</title>
<link rel="stylesheet" href="https://fonts.googleapis.com/css2?family=Montserrat:wght@400;600;800&family=Open+Sans:wght@400;600;700&display=swap">
<style>
:root{
  --board:#e9e4dc;
  --navy:#163a70;
  --blue:#1f5fae;
  --green:#6cb33f;
  --green-dark:#3f8a2a;
  --red:#c8202a;
  --tan:#d8c7a5;
  --white:#ffffff;
  --ink:#2b2b2b;
  --muted:#6b6b6b;
}
*{box-sizing:border-box;margin:0;padding:0}
html,body{width:1200px;height:509px;overflow:hidden}
body{background:var(--board);font-family:"Open Sans",Arial,sans-serif;color:var(--ink);position:relative}
.board-title{position:absolute;top:4px;left:0;width:1200px;text-align:center;font:800 20px "Montserrat",Arial,sans-serif;color:var(--navy)}
.label{position:absolute;font:600 11px "Open Sans",Arial,sans-serif;color:var(--ink);white-space:nowrap}
.piece{position:absolute;overflow:hidden;background:var(--white);box-shadow:0 2px 5px rgba(0,0,0,.3)}
.brand{display:flex;align-items:center;gap:3px;font:700 9px "Open Sans",Arial,sans-serif;color:var(--navy)}
.brand-dot{width:9px;height:9px;border-radius:50%;background:var(--green)}
.fill{position:absolute}

/* postcard front */
.pc{width:330px;height:214px}
.pc-front .house{left:120px;top:60px;width:210px;height:112px;background:linear-gradient(#bcd7ef,#8aa6be 60%,#6f8d5a)}
.pc-front .agent{left:12px;top:26px;width:105px;height:146px;background:linear-gradient(#c9b39c,#7a5c48)}
.pc-front .brand{position:absolute;left:8px;top:6px;background:var(--white);padding:2px 5px;border-radius:2px}
.headline{position:absolute;left:126px;top:6px;font-family:"Montserrat",Arial,sans-serif;color:var(--navy);line-height:1}
.headline .small{font-weight:800;font-size:16px}
.headline .big{font-weight:800;font-size:30px;color:var(--blue)}
.headline .sub{font-weight:600;font-size:7px;letter-spacing:.5px}
.sale-sign{position:absolute;left:245px;top:102px;width:70px;height:52px;background:var(--white);border:3px solid var(--red);text-align:center;font:800 11px/1.1 "Montserrat",Arial,sans-serif;color:var(--red);padding-top:6px}
.front-band{position:absolute;left:0;bottom:0;width:100%;height:42px;background:var(--navy);color:var(--white);padding:4px 10px}
.front-band p{font-size:7px}
.front-band .join{font:800 13px "Montserrat",Arial,sans-serif;white-space:nowrap}
.front-band .join span{color:var(--green)}

/* postcard back */
.pc-back .brand{position:absolute;left:8px;top:8px}
.pc-back .photo{left:110px;top:18px;width:110px;height:78px;background:linear-gradient(#c8dcef,#8ba0ad 55%,#6c8750)}
.signup{position:absolute;left:228px;top:30px;width:62px;height:62px;border-radius:50%;background:var(--green);color:var(--white);text-align:center;font:800 12px/1.05 "Montserrat",Arial,sans-serif;padding-top:12px}
.stamp{position:absolute;right:8px;top:8px;width:26px;height:20px;border:1px solid var(--muted);font-size:5px;text-align:center;padding-top:3px;color:var(--muted)}
.alert{position:absolute;left:8px;top:104px;width:140px;background:var(--green);color:var(--white);font:700 7px/1.25 "Open Sans",Arial,sans-serif;padding:4px 6px;border-radius:3px}
.agent-lines{position:absolute;left:8px;top:26px;font-size:7px;line-height:1.4}
.agent-lines strong{font-size:8px;color:var(--navy)}
.address{position:absolute;left:180px;top:108px;font-size:7px;line-height:1.5}
.disclaimer{position:absolute;left:8px;top:142px;width:160px;font-size:5px;color:var(--muted)}
.back-band{position:absolute;left:0;bottom:0;width:100%;height:48px;background:var(--blue);color:var(--white);padding:6px 10px}
.back-band .tag{font:700 10px "Montserrat",Arial,sans-serif}
.back-band .url{font:800 11px "Montserrat",Arial,sans-serif;color:var(--tan)}
.is-green .back-band{background:var(--green-dark)}
.is-green .signup{background:var(--blue)}

/* business cards */
.bc{width:142px;height:81px}
.bc-front .brand{position:absolute;left:6px;top:6px;font-size:8px}
.bc-front .details{position:absolute;right:6px;top:6px;text-align:right;font-size:5.5px;line-height:1.45}
.bc-front .details strong{font-size:7px;color:var(--navy)}
.wave{position:absolute;left:0;bottom:0;width:100%;height:26px}
.bc-back{background:var(--blue);display:flex;align-items:center;justify-content:center}
.is-green .bc-back{background:var(--green)}
.bc-back .team-name{font:700 12px "Open Sans",Arial,sans-serif;color:var(--white)}

/* email signature */
.sig{width:165px;height:50px}
.sig .brand{position:absolute;left:6px;top:8px;font-size:8px}
.sig .details{position:absolute;left:80px;top:6px;font-size:5.5px;line-height:1.4}
.sig .details strong{font-size:7px;color:var(--navy)}
.sig .wave{height:14px}
</style>
</head>
<body>
<h1 class="board-title">Post Card</h1>

<section class="set">
  <span class="label" style="left:12px;top:26px">Front</span>
  <article class="piece pc pc-front" style="left:12px;top:40px">
    <div class="fill house" role="img" aria-label="Photo of a two-storey suburban house"></div>
    <div class="fill agent" role="img" aria-label="Photo of the real estate agent"></div>
    <div class="brand"><span class="brand-dot"></span>BrightHarbor</div>
    <div class="headline"><div class="small">SEARCH</div><div class="big">HUNDREDS</div><div class="sub">OF BANK OWNED FORECLOSURES</div></div>
    <div class="sale-sign">HOME<br>FOR<br>SALE</div>
    <div class="front-band"><p>Don't miss this opportunity to buy a bank owned foreclosure.</p><div class="join">JOIN <span>FindMarlowHomesteads.example</span></div></div>
  </article>

  <span class="label" style="left:372px;top:26px">Back</span>
  <article class="piece pc pc-back" style="left:372px;top:40px">
    <div class="brand"><span class="brand-dot"></span>BrightHarbor</div>
    <div class="agent-lines"><strong>Dana Holloway</strong><br>Foreclosure Specialist<br>843-555-0142</div>
    <div class="fill photo" role="img" aria-label="Photo of the new listing"></div>
    <div class="signup">SIGN<br>UP<br>FREE!</div>
    <div class="stamp">PRSRT STD</div>
    <div class="alert">NEW LISTING ALERT – Sign up and receive listings meeting your criteria today!</div>
    <div class="address">Resident Name<br>123 Sample Street<br>Marlow, SC 29401</div>
    <p class="disclaimer">This property is NOT listed in MLS yet. Please contact me if you are interested in purchasing this property.</p>
    <div class="back-band"><div class="tag">We are your Charleston Foreclosure Specialist!</div><div class="url">FINDMARLOWHOMESTEADS.EXAMPLE</div></div>
  </article>

  <span class="label" style="left:720px;top:26px">Business Card Front</span>
  <span class="label" style="left:872px;top:26px">Business Card Front</span>
  <article class="piece bc bc-front" style="left:720px;top:40px">
    <div class="brand"><span class="brand-dot"></span>BrightHarbor</div>
    <div class="details"><strong>Dana Holloway</strong><br>Broker Associate<br>843-555-0142<br>dana@brightharbor.example<br>1 Harbor Way, Marlow SC</div>
    <svg class="wave" viewBox="0 0 142 26" preserveAspectRatio="none"><path d="M0 14 Q50 0 142 12 V26 H0Z" fill="var(--green)"/><path d="M0 20 Q60 8 142 18 V26 H0Z" fill="var(--blue)"/></svg>
  </article>
  <article class="piece bc bc-front" style="left:872px;top:40px">
    <div class="brand"><span class="brand-dot"></span>BrightHarbor</div>
    <div class="details"><strong>Dana Holloway</strong><br>Broker Associate<br>843-555-0142<br>dana@brightharbor.example<br>1 Harbor Way, Marlow SC</div>
    <svg class="wave" viewBox="0 0 142 26" preserveAspectRatio="none"><path d="M0 14 Q50 0 142 12 V26 H0Z" fill="var(--blue)"/><path d="M0 20 Q60 8 142 18 V26 H0Z" fill="var(--green)"/></svg>
  </article>

  <span class="label" style="left:720px;top:128px">Business Card Back</span>
  <span class="label" style="left:872px;top:128px">Business Card Back</span>
  <article class="piece bc bc-back" style="left:720px;top:142px"><span class="team-name">Holloway</span></article>
  <article class="piece bc bc-back" style="left:872px;top:142px"><span class="team-name">Holloway</span></article>

  <span class="label" style="left:1025px;top:94px">Email Signature</span>
  <article class="piece sig" style="left:1025px;top:108px">
    <div class="brand"><span class="brand-dot"></span>BrightHarbor</div>
    <div class="details"><strong>Dana Holloway</strong><br>Broker Associate<br>843-555-0142</div>
    <svg class="wave" viewBox="0 0 165 14" preserveAspectRatio="none"><path d="M0 8 Q60 0 165 6 V14 H0Z" fill="var(--green)"/><path d="M0 12 Q70 4 165 10 V14 H0Z" fill="var(--blue)"/></svg>
  </article>
</section>

<section class="set is-green">
  <span class="label" style="left:12px;top:266px">Front</span>
  <article class="piece pc pc-front" style="left:12px;top:280px">
    <div class="fill house" role="img" aria-label="Photo of a two-storey suburban house"></div>
    <div class="fill agent" role="img" aria-label="Photo of the real estate agent"></div>
    <div class="brand"><span class="brand-dot"></span>BrightHarbor</div>
    <div class="headline"><div class="small">SEARCH</div><div class="big">HUNDREDS</div><div class="sub">OF BANK OWNED FORECLOSURES</div></div>
    <div class="sale-sign">HOME<br>FOR<br>SALE</div>
    <div class="front-band"><p>Don't miss this opportunity to buy a bank owned foreclosure.</p><div class="join">JOIN <span>FindMarlowHomesteads.example</span></div></div>
  </article>

  <span class="label" style="left:372px;top:266px">Back</span>
  <article class="piece pc pc-back" style="left:372px;top:280px">
    <div class="brand"><span class="brand-dot"></span>BrightHarbor</div>
    <div class="agent-lines"><strong>Dana Holloway</strong><br>Foreclosure Specialist<br>843-555-0142</div>
    <div class="fill photo" role="img" aria-label="Photo of the new listing"></div>
    <div class="signup">SIGN<br>UP<br>FREE!</div>
    <div class="stamp">PRSRT STD</div>
    <div class="alert">NEW LISTING ALERT – Sign up and receive listings meeting your criteria today!</div>
    <div class="address">Resident Name<br>123 Sample Street<br>Marlow, SC 29401</div>
    <p class="disclaimer">This property is NOT listed in MLS yet. Please contact me if you are interested in purchasing this property.</p>
    <div class="back-band"><div class="tag">We are your Charleston Foreclosure Specialist!</div><div class="url">FINDMARLOWHOMESTEADS.EXAMPLE</div></div>
  </article>

  <span class="label" style="left:720px;top:266px">Business Card Front</span>
  <span class="label" style="left:872px;top:266px">Business Card Front</span>
  <article class="piece bc bc-front" style="left:720px;top:280px">
    <div class="brand"><span class="brand-dot"></span>BrightHarbor</div>
    <div class="details"><strong>Dana Holloway</strong><br>Broker Associate<br>843-555-0142<br>dana@brightharbor.example<br>1 Harbor Way, Marlow SC</div>
    <svg class="wave" viewBox="0 0 142 26" preserveAspectRatio="none"><path d="M0 14 Q50 0 142 12 V26 H0Z" fill="var(--blue)"/><path d="M0 20 Q60 8 142 18 V26 H0Z" fill="var(--green)"/></svg>
  </article>
  <article class="piece bc bc-front" style="left:872px;top:280px">
    <div class="brand"><span class="brand-dot"></span>BrightHarbor</div>
    <div class="details"><strong>Dana Holloway</strong><br>Broker Associate<br>843-555-0142<br>dana@brightharbor.example<br>1 Harbor Way, Marlow SC</div>
    <svg class="wave" viewBox="0 0 142 26" preserveAspectRatio="none"><path d="M0 14 Q50 0 142 12 V26 H0Z" fill="var(--green)"/><path d="M0 20 Q60 8 142 18 V26 H0Z" fill="var(--green-dark)"/></svg>
  </article>

  <span class="label" style="left:720px;top:368px">Business Card Back</span>
  <span class="label" style="left:872px;top:368px">Business Card Back</span>
  <article class="piece bc bc-back" style="left:720px;top:382px"><span class="team-name">Holloway</span></article>
  <article class="piece bc bc-back" style="left:872px;top:382px"><span class="team-name">Holloway</span></article>

  <span class="label" style="left:1025px;top:334px">Email Signature</span>
  <article class="piece sig" style="left:1025px;top:348px">
    <div class="brand"><span class="brand-dot"></span>BrightHarbor</div>
    <div class="details"><strong>Dana Holloway</strong><br>Broker Associate<br>843-555-0142</div>
    <svg class="wave" viewBox="0 0 165 14" preserveAspectRatio="none"><path d="M0 8 Q60 0 165 6 V14 H0Z" fill="var(--green)"/><path d="M0 12 Q70 4 165 10 V14 H0Z" fill="var(--green-dark)"/></svg>
  </article>
</section>
</body>
</html>
```